Website design for Cambridge based systematic hedge fund

We have run previous craftmosaic competitions to design our company logo, business cards and the styling of our presentation deck (see attached files).
As the final step we are looking to get a website designed that is thematically consistent with these existing elements of our branding.
You can find some of our competitors websites below:
https://www.quelmarsh.example/
https://www.fenloor.example/
https://www.pyvart.example/
https://www.dulvet.example/
https://www.orbelmfunds.example/
https://www.valtrigo.example/
https://www.meskilfunds.example/home
We would like to have a website that works well on both mobile devices and desktops. Either just as one page that can be scrolled down, with links at the top that skips to certain sections, or a few separate pages that can be navigated by a top menu.
It should look professional, we are not after lots of animations or unnecessary transitions, and in particular the website must be smooth to navigate. We would like to avoid having peoples of people, we are happy to make use of elements from the presentation (for example the style of the cover slide, or the section slides with the faded bridge in the background), or 'financial' style images.
We would like to have the following sections for now. For some of these some example text has been provided, final text may change but it will be of similar length. For the other sections we are happy to just have template text for now. At the moment we are mainly interested to see styles/layouts as words can be added easily afterwards:
1) We will need a disclaimer pop up the first time someone visits the site (see for example the meskilfunds example).
2) Top page - company name, then in larger text "Bringing AI and Statistical Inference to Financial Markets", and somewhere in smaller text "Harlow Vectors is a quantitative asset manager with the singular focus of delivering algorithmic strategies that work"
3) "About us" section: will describe us as a company, details our approach, company values, and explains the company logo.
Example text:
"We deliver consistent alpha across liquid markets through the application of proprietary IP in Bayesian inference, machine learning and artificial intelligence. We are a multi-disciplinary team founded by experienced finance professionals from premier institutions, leading academics from the Thornbury Stellar Unit at Ashmere College and world-class software engineers.
Our logo portrays a sillhoute of the lattice walkway at Ashmere College. Our unique scientific approach allows us to bridge cutting-edge mathematical research and computing expertise with financial knowledge to bring algorithmns that work to liquid markets"
4) Hiring section, detailing our culture, what we are looking for.
Example text:
"We are always looking for exceptional talent to join our entrepreneurial team. We are looking for individuals who are creative thinkers, can demonstrate analytical rigour and are passionate about the intersection of science, finance and technology.
We prioritise having a company culture that promotes sharing ideas in a safe, collaborative research environment. We make sure that every member of the team has the oppertunity to explore their own ideas through weekly 'innovation time', and ensure that everyone gets the support they need to continue to grow as individuals within the company."
5) A section for news/press releases
6) Contact us area at the bottom with office location and email. We will need to list 3 addresses for our Cambridge, London and Singapore offices, along with a couple of contact emails or phone numbers
7) A client login button at the top that will take them to a different website (unrelated to this one).

```html
<!DOCTYPE html>
<html lang="en">
<head>
<meta charset="utf-8">
<title>Harlow Vectors — Phone Version</title>
<link href="https://fonts.googleapis.com/css2?family=Montserrat:wght@400;500;600;700;800&display=swap" rel="stylesheet">
<style>
:root{
  --page:#cfe0f4;
  --navy:#0c356a;
  --blue:#2d7ed8;
  --sky:#e6f0fb;
  --ink:#51606f;
  --line:#7fb2ea;
  --white:#ffffff;
}
*{box-sizing:border-box;margin:0;padding:0}
html,body{width:1200px;height:2684px;overflow:hidden}
body{background:var(--page);font-family:"Montserrat",sans-serif;color:var(--ink);position:relative}
.version-label{position:absolute;left:32px;top:28px;font-size:24px;font-weight:700;color:var(--navy)}
.phone{position:absolute;background:var(--white);overflow:hidden}
.phone--left{left:160px;top:100px;width:500px;height:2584px}
.phone--right{left:712px;top:0;width:450px;height:2520px}

.hero{height:520px;background:linear-gradient(180deg,#f2f7fd,#dbe9f8);position:relative;overflow:hidden}
.hero__photo{position:absolute;right:0;top:0;width:190px;height:520px;background:linear-gradient(180deg,#9fc3ea,#6d9bd0 50%,#cfe0f4)}
.brand{position:absolute;left:30px;top:26px;width:120px;height:84px;background:var(--navy);display:flex;align-items:center;justify-content:center;text-align:center;color:var(--white);font-size:13px;font-weight:700;letter-spacing:1px;line-height:1.3}
.hero__title{position:absolute;left:30px;top:165px;width:270px;font-size:30px;line-height:1.18;font-weight:800;color:var(--navy)}
.hero__text{position:absolute;left:30px;top:370px;width:240px;font-size:11.5px;line-height:1.5}
.hero__btn{position:absolute;left:30px;top:450px;border:1.5px solid var(--navy);border-radius:16px;padding:6px 18px;font-size:10px;font-weight:600;color:var(--navy)}

.section{padding:0 30px;position:relative}
.section-title{font-size:24px;font-weight:700;color:var(--navy);position:relative;margin:60px 0 24px}
.section-title span{color:var(--blue)}
.section-title::before{content:"";position:absolute;left:-70px;top:50%;width:62px;height:2px;background:var(--line)}
.body-text{font-size:14px;line-height:1.7}

.circle-photo{width:320px;height:320px;border-radius:50%;margin:0 auto 36px;background:radial-gradient(circle at 50% 40%,#d9c7b3,#8fa7bf 70%);border:8px solid var(--sky)}
.jobs{margin-top:26px;display:flex;flex-direction:column;gap:20px}
.job{background:var(--sky);border-left:4px solid var(--blue);padding:18px 20px}
.job__title{font-size:14px;font-weight:700;color:var(--navy)}
.job__place{display:flex;align-items:center;gap:6px;font-size:12px;margin-top:10px;color:var(--blue)}
.framed-photo{margin:30px auto 0;width:310px;height:250px;border:8px solid var(--sky);background:linear-gradient(135deg,#3a5578,#8fb0d6 55%,#dfe9f5)}
.news-card{margin-top:10px}
.news-card__img{height:210px;background:linear-gradient(135deg,#9bc0e8,#e7f0fb)}
.news-card__img--robot{background:linear-gradient(135deg,#e9eef4,#b8c8da)}
.news-card__title{font-size:15px;font-weight:700;color:var(--navy);margin:18px 0 10px}
.news-card__text{font-size:12px;line-height:1.6}
.news-card__more{text-align:right;font-size:12px;font-weight:600;color:var(--navy);margin-top:14px;padding-bottom:10px;border-bottom:1.5px solid var(--line)}

.contact{background:var(--navy);color:var(--white);padding:44px 36px;margin-top:56px}
.office{margin-bottom:34px}
.office:last-child{margin-bottom:0}
.office__name{font-size:16px;font-weight:700;margin-bottom:14px}
.office__row{display:flex;gap:10px;align-items:flex-start;font-size:12px;line-height:1.5;margin-bottom:10px}
.office__row svg{flex:none;margin-top:2px}

.footer{padding:44px 36px}
.footer .brand{position:static;width:120px;height:68px;font-size:12px;margin-bottom:22px}
.footer__text{font-size:12px;line-height:1.6;margin-bottom:20px}
.footer__head{font-size:15px;font-weight:700;color:var(--navy);margin:18px 0 10px}
.footer__list{list-style:none;font-size:12px;line-height:2}
</style>
</head>
<body>
<div class="version-label">Phone Version</div>

<main class="phone phone--left">
  <header class="hero">
    <div class="hero__photo" role="img" aria-label="Photo of a tall glass office tower against a blue sky"></div>
    <div class="brand">HARLOW<br>VECTORS</div>
    <h1 class="hero__title">Bringing AI and Statistical Inference to Financial Markets</h1>
    <p class="hero__text">Harlow Vectors is a quantitative asset manager with the singular focus of delivering algorithmic strategies that work</p>
    <a class="hero__btn">Get in touch</a>
  </header>

  <section class="section">
    <h2 class="section-title">What <span>We Do?</span></h2>
    <div class="circle-photo" role="img" aria-label="Round photo of the team at work in the office"></div>
    <p class="body-text">We deliver consistent alpha across liquid markets through the application of proprietary IP in Bayesian inference, machine learning and artificial intelligence. We are a multi-disciplinary team founded by experienced finance professionals from premier institutions, leading academics from the Thornbury Stellar Unit at Ashmere College and world-class software engineers.</p>
  </section>

  <section class="section">
    <h2 class="section-title">Our Open <span>Positions</span></h2>
    <p class="body-text">We are always looking for exceptional talent to join our entrepreneurial team. We are looking for individuals who are creative thinkers, can demonstrate analytical rigour and are passionate about the intersection of science, finance and technology.</p>
    <div class="jobs">
      <div class="job"><div class="job__title">Growth Marketer</div><div class="job__place"><svg width="10" height="13" viewBox="0 0 10 13"><path d="M5 0a5 5 0 0 0-5 5c0 3.5 5 8 5 8s5-4.5 5-8a5 5 0 0 0-5-5zm0 7a2 2 0 1 1 0-4 2 2 0 0 1 0 4z" fill="currentColor"/></svg>Cambridge</div></div>
      <div class="job"><div class="job__title">Software Engineer (Computer Science)</div><div class="job__place"><svg width="10" height="13" viewBox="0 0 10 13"><path d="M5 0a5 5 0 0 0-5 5c0 3.5 5 8 5 8s5-4.5 5-8a5 5 0 0 0-5-5zm0 7a2 2 0 1 1 0-4 2 2 0 0 1 0 4z" fill="currentColor"/></svg>London</div></div>
      <div class="job"><div class="job__title">Growth Marketer</div><div class="job__place"><svg width="10" height="13" viewBox="0 0 10 13"><path d="M5 0a5 5 0 0 0-5 5c0 3.5 5 8 5 8s5-4.5 5-8a5 5 0 0 0-5-5zm0 7a2 2 0 1 1 0-4 2 2 0 0 1 0 4z" fill="currentColor"/></svg>Singapore</div></div>
    </div>
  </section>

  <section class="section">
    <h2 class="section-title">Our <span>Culture</span></h2>
    <p class="body-text">We prioritise having a company culture that promotes sharing ideas in a safe, collaborative research environment. We make sure that every member of the team has the opportunity to explore their own ideas through weekly innovation time, and ensure that everyone gets the support they need to continue to grow as individuals within the company.</p>
    <div class="framed-photo" role="img" aria-label="Photo of a trading screen with market charts"></div>
  </section>

  <section class="section">
    <h2 class="section-title">Our Latest <span>News</span></h2>
    <article class="news-card">
      <div class="news-card__img" role="img" aria-label="Photo of a hand touching a digital interface"></div>
      <h3 class="news-card__title">How is AI changing the Financial World</h3>
      <p class="news-card__text">Lorem Ipsum is simply dummy text of the printing and typesetting industry. Lorem Ipsum has been the industry.</p>
    </article>
  </section>
</main>

<aside class="phone phone--right">
  <section class="section">
    <h2 class="section-title" style="margin-top:44px">Our <span>Culture</span></h2>
    <p class="body-text">We prioritise having a company culture that promotes sharing ideas in a safe, collaborative research environment. We make sure that every member of the team has the opportunity to explore their own ideas through weekly innovation time, and ensure that everyone gets the support they need to continue to grow as individuals within the company.</p>
    <div class="framed-photo" style="width:270px;height:210px" role="img" aria-label="Photo of a trading screen with market charts"></div>
  </section>

  <section class="section">
    <h2 class="section-title">Our Latest <span>News</span></h2>
    <article class="news-card">
      <div class="news-card__img" role="img" aria-label="Photo of a hand touching a digital interface"></div>
      <h3 class="news-card__title">How is AI changing the Financial World</h3>
      <p class="news-card__text">Lorem Ipsum is simply dummy text of the printing and typesetting industry. Lorem Ipsum has been the industry.</p>
      <div class="news-card__more">Continue reading →</div>
    </article>
    <article class="news-card" style="margin-top:40px">
      <div class="news-card__img news-card__img--robot" role="img" aria-label="Photo of a white humanoid robot"></div>
      <h3 class="news-card__title">How is AI changing the Financial World</h3>
      <p class="news-card__text">Lorem Ipsum is simply dummy text of the printing and typesetting industry. Lorem Ipsum has been the industry.</p>
      <div class="news-card__more">Continue reading →</div>
    </article>
  </section>

  <section class="contact">
    <div class="office">
      <h3 class="office__name">Cambridge Office</h3>
      <div class="office__row"><svg width="11" height="14" viewBox="0 0 10 13"><path d="M5 0a5 5 0 0 0-5 5c0 3.5 5 8 5 8s5-4.5 5-8a5 5 0 0 0-5-5zm0 7a2 2 0 1 1 0-4 2 2 0 0 1 0 4z" fill="#fff"/></svg>48 Fernbrook Lane<br>Unit 7 Tessel Row</div>
      <div class="office__row"><svg width="13" height="10" viewBox="0 0 13 10"><rect x=".5" y=".5" width="12" height="9" fill="none" stroke="#fff"/><path d="M.5.5l6 5 6-5" fill="none" stroke="#fff"/></svg>contact@harlowvectors.example</div>
      <div class="office__row"><svg width="12" height="12" viewBox="0 0 12 12"><path d="M2 1l2 0 1 3-1.5 1a7 7 0 0 0 3.5 3.5L8 7l3 1v2a1 1 0 0 1-1 1A9 9 0 0 1 1 2a1 1 0 0 1 1-1z" fill="#fff"/></svg>+00 100 555 01</div>
    </div>
    <div class="office">
      <h3 class="office__name">London Office</h3>
      <div class="office__row"><svg width="11" height="14" viewBox="0 0 10 13"><path d="M5 0a5 5 0 0 0-5 5c0 3.5 5 8 5 8s5-4.5 5-8a5 5 0 0 0-5-5zm0 7a2 2 0 1 1 0-4 2 2 0 0 1 0 4z" fill="#fff"/></svg>48 Fernbrook Lane<br>Unit 7 Tessel Row</div>
      <div class="office__row"><svg width="13" height="10" viewBox="0 0 13 10"><rect x=".5" y=".5" width="12" height="9" fill="none" stroke="#fff"/><path d="M.5.5l6 5 6-5" fill="none" stroke="#fff"/></svg>contact@harlowvectors.example</div>
      <div class="office__row"><svg width="12" height="12" viewBox="0 0 12 12"><path d="M2 1l2 0 1 3-1.5 1a7 7 0 0 0 3.5 3.5L8 7l3 1v2a1 1 0 0 1-1 1A9 9 0 0 1 1 2a1 1 0 0 1 1-1z" fill="#fff"/></svg>+00 100 555 01</div>
    </div>
    <div class="office">
      <h3 class="office__name">Singapore Office</h3>
      <div class="office__row"><svg width="11" height="14" viewBox="0 0 10 13"><path d="M5 0a5 5 0 0 0-5 5c0 3.5 5 8 5 8s5-4.5 5-8a5 5 0 0 0-5-5zm0 7a2 2 0 1 1 0-4 2 2 0 0 1 0 4z" fill="#fff"/></svg>48 Fernbrook Lane<br>Unit 7 Tessel Row</div>
      <div class="office__row"><svg width="12" height="12" viewBox="0 0 12 12"><path d="M2 1l2 0 1 3-1.5 1a7 7 0 0 0 3.5 3.5L8 7l3 1v2a1 1 0 0 1-1 1A9 9 0 0 1 1 2a1 1 0 0 1 1-1z" fill="#fff"/></svg>+00 100 555 01</div>
    </div>
  </section>

  <footer class="footer">
    <div class="brand">HARLOW<br>VECTORS</div>
    <p class="footer__text">Lorem Ipsum is simply dummy text of the printing and typesetting industry. Lorem Ipsum has been the industry's standard dummy text ever since the 1500s, when an unknown printer took a galley of type and scrambled it to make a type specimen book.</p>
    <h4 class="footer__head">Usefull Links</h4>
    <ul class="footer__list"><li>Clients Space</li><li>Latest News</li><li>Privacy Policy</li></ul>
    <h4 class="footer__head">Site Map</h4>
    <ul class="footer__list"><li>Our Culture</li><li>Our Open Job Positions</li><li>What does Our Logo Mean</li><li>Our Values</li></ul>
    <h4 class="footer__head">Usefull Links</h4>
    <ul class="footer__list"><li>Clients Space</li><li>Latest News</li><li>Privacy Policy</li></ul>
  </footer>
</aside>
</body>
</html>
```